B2B EDM Banner Design- Specialist Tech Company

We need a new top-of-email banner for our EDM campaigns for Varnel Brix (www.varnelbrix-example.com
). This banner will sit at the top of every email and must immediately signal the brand, look modern and professional, and be visually aligned with the tech/IT audience.
Size of the banner: Around 728x90 - it must fit at the top of an email blast.
Purpose of the Banner
Establish a strong, recognizable brand identity across all Varnel Brix EDMs
visually consistent with existing banners created for other brands (see reference examples provided)
Communicate Varnel Brix’s value proposition at a glance
Brand Name
Varnel Brix
Tagline (must appear in the banner)
“11,322 whitepapers from 726 companies”
Design Requirements
Style & Tone
Modern, clean, and professional
Tech-centric look and feel
High-quality, sleek, and corporate
Eye-catching but not cluttered
Should feel premium and authoritative
Layout & Composition
Full-width banner for email header
Horizontal orientation similar to the Plomtar and Quindle Staff Archive examples
Include space for the brand name/logo prominently on the left or centered
Integrate the tagline in a readable, secondary position
Optional: a subtle background texture or tech-related abstract pattern (circuitry, network nodes, gradient, etc.)
No busy imagery—should feel clean and trustworthy
Color Palette
Use colors consistent with Varnel Brix branding from www.varnelbrix-example.com
Blues, greys, blacks, and tech-style gradients preferred
Should feel consistent with a B2B IT audience
Typography
Clean, sans-serif fonts (professional/tech-aligned)
Brand name should be bold and prominent
Tagline should be smaller, but still readable on desktop and mobile
Imagery (if used)
Abstract tech shapes, network visuals, geometric patterns, or gradient overlays
Avoid photography of people
Keep imagery subtle so text remains legible
Call-to-Action Button (optional)
None required in this banner (unlike the HR examples)
Banner should remain a pure brand header
Deliverables
Final banner in PNG and JPG formats
2–3 design variations (if possible) for A/B testing
Dimensions optimized for EDM: ~600–700px wide (standard email width), proportionate height

```html
<!DOCTYPE html>
<html lang="en">
<head>
<meta charset="utf-8">
<title>Varnel Brix – EDM Header Banner</title>
<link rel="stylesheet" href="https://fonts.googleapis.com/css2?family=Montserrat:wght@500;600;700;800&display=swap">
<style>
  :root {
    --navy-deep: #071227;
    --navy-mid: #0b1f3d;
    --navy-light: #12315a;
    --white: #ffffff;
    --cyan: #1fb6ee;
    --glow: #5fe0ff;
    --muted: #c9d6e6;
  }
  * { margin: 0; padding: 0; box-sizing: border-box; }
  html, body { width: 1200px; height: 148px; overflow: hidden; background: var(--navy-deep); }
  .banner {
    position: relative;
    width: 1200px;
    height: 148px;
    overflow: hidden;
    font-family: "Montserrat", Arial, sans-serif;
    background: linear-gradient(90deg, var(--navy-deep) 0%, var(--navy-mid) 45%, var(--navy-light) 75%, var(--navy-mid) 100%);
  }
  .brand {
    position: absolute;
    left: 48px;
    top: 40px;
    display: flex;
    align-items: center;
    gap: 16px;
  }
  .brand-dot {
    width: 50px;
    height: 50px;
    border-radius: 50%;
    background: var(--cyan);
  }
  .brand-name {
    color: var(--white);
    font-weight: 800;
    font-size: 30px;
    letter-spacing: 0.5px;
    line-height: 1;
  }
  .brand-sub {
    color: var(--white);
    font-weight: 600;
    font-size: 11.5px;
    letter-spacing: 2.6px;
    margin-top: 9px;
  }
  .tech-wave {
    position: absolute;
    left: 470px;
    top: 0;
    width: 460px;
    height: 148px;
    background:
      radial-gradient(ellipse 120px 60px at 48% 55%, rgba(95,224,255,0.55), rgba(31,182,238,0.15) 60%, transparent 100%),
      radial-gradient(ellipse 220px 40px at 55% 40%, rgba(31,182,238,0.25), transparent 100%);
  }
  .tagline {
    position: absolute;
    left: 775px;
    top: 44px;
    color: var(--white);
    font-weight: 500;
    font-size: 23px;
    line-height: 29px;
    letter-spacing: 0.6px;
    text-transform: uppercase;
  }
  .tagline .figure { color: var(--cyan); font-weight: 700; }
</style>
</head>
<body>
  <div class="banner">
    <div class="brand">
      <span class="brand-dot"></span>
      <div>
        <div class="brand-name">VARNEL BRIX</div>
        <div class="brand-sub">FOR IT PROFESSIONALS</div>
      </div>
    </div>
    <div class="tech-wave" role="img" aria-label="Abstract glowing particle wave of cyan light suggesting digital data flow"></div>
    <p class="tagline">
      <span class="figure">11322</span> Whitepapers from<br>
      <span class="figure">726</span> Companies
    </p>
  </div>
</body>
</html>
```